Update Existing Homepage

Here’s the scoop… we want to update our homepage here with a more modern look: wws.Pagelore-Hub.com

I am NOT looking for a brand new design; as our site has many pages, and section. Instead I want a new more modern design based on the existing design (if that make sense)

Whatever new design…must match the rest of the site
I want the current header (menu and up) as well as the current footer to stay the same; it’s everything in between that has to change.

What I’m really looking for is:

- Better use of space
- Better emphasis on key components
- Addition of a new section (more about that below)
- More modern feel

By modern I mean the icons we use are getting a bit cheesy, the straight layout is also dated, etc

Here are the elements that I need to have on the page in ORDER OF IMPORTANCE:

1) ADVERTISING SPACE: while I don’t want huge flashing ads front and center, this being an information site, ads are our #1 source of revenue and as such are important. I would like to see several add slots of various sizes (standard sizes) throughout the page in eye catching spots (not hidden in the bottom right corner)

2) ARTICLES: articles are our main draw. If you look at the current design you will see there is a lead article at the top left of the page and then a series of other articles down the middle

3) NEWSLETTER SUBSCRIPTION BOX: need to have a section that is highly visible for people to subscribe to our newsletter (doesn’t have to be as big as the existing one)

4) BLOG POSTS (‘the experts say’ section): besides articles we also have blog posts. However I’m thinking we could combine the articles and the blog posts into 1 section titled “news” or something to save space. And the blog posts could just have an identifier at the beginning of the title such as “Blog: post title”

5) VIDEOS: don’t need to show a ton of vids, but would like room for 1 main video and a few suggestions of others.

What I have seen a bunch of new websites use is a type rotating ‘newsboard’, like the one on the quorvex homepage for example. Perhaps using an idea like that could be cool. You could feature 1 article, 1 blog post, 1 video, or something in it and have it rotate.

6) RESOURCES: This is something that is not ‘really’ currently on the homepage. By that I mean there is a “webmaster resources” section + a “webmaster tools” section but these are dated. Dated because we recently added a new directory to the site: http://resources.pagelore-hub.com/ - so what I would like to do now is combine those 2 section; 1) invite people to check out the directory + submit there and 2) list a few of the newer entries (ie. new entries automatically get posted on the section of our homepage

7) FORUM DISCUSSIONS: if you look at the “Industry Discussions and Help” section, those are the latest discussions from our forums http://forums.pagelore-hub.com/

That is it…good luck,

Tev

Target Market(s)

web professionals

Industry/Entity Type

Industry

Requirements
Must have
• see description
Nice to have
• see description
Should not have
• see description

```html
<!DOCTYPE html>
<html lang="en">
<head>
<meta charset="utf-8">
<title>Pagelore Hub – Helping You Succeed Online</title>
<link href="https://fonts.googleapis.com/css2?family=Arimo:wght@400;700&family=Oswald:wght@500;700&family=Ubuntu:wght@400;500;700&display=swap" rel="stylesheet">
<style>
:root{
  --lime:#c9de2e;
  --lime-light:#dcec55;
  --lime-pale:#f3f8d2;
  --purple:#8a1f6d;
  --purple-dark:#6e1757;
  --ink:#111;
  --muted:#666;
  --rule:#e3e3e3;
  --panel:#f4f4f4;
  --page-bg:#f3f3f3;
}
*{box-sizing:border-box;margin:0;padding:0}
html,body{width:854px;height:1200px;overflow:hidden;background:#fff}
body{font-family:"Arimo",Arial,sans-serif;color:var(--ink);position:relative}
ul{list-style:none}

/* header (unchanged) */
.top-band{position:absolute;left:0;top:0;width:854px;height:77px;background:linear-gradient(#f6f6f6,#fff 40%)}
.header{position:absolute;left:85px;top:5px;width:689px;height:72px;background:#fff;border-top:1px solid #e6e6e6}
.brand{position:absolute;left:57px;top:19px;display:flex;align-items:center;gap:6px}
.brand-mark{width:14px;height:14px;background:var(--purple)}
.brand-name{font-size:20px;color:#333}
.tagline{position:absolute;left:57px;top:53px;font-size:10px;letter-spacing:1.4px;color:#777}
.search{position:absolute;left:376px;top:10px;width:300px;height:26px;background:#eee;border-radius:3px}
.search-field{position:absolute;left:32px;top:6px;width:174px;height:12px;background:#fff;border:1px solid #ccc}
.search-btn{position:absolute;right:0;top:0;width:66px;height:26px;background:var(--lime);font-size:7px;color:#333;display:flex;align-items:center;justify-content:center;border-radius:0 3px 3px 0}
.social{position:absolute;left:544px;top:45px;display:flex;gap:4px}
.social span{width:22px;height:22px;border-radius:3px}
.lang{position:absolute;left:630px;top:50px;font-size:10px;color:#444;display:flex;align-items:center;gap:4px}
.lang i{width:9px;height:9px;border-radius:50%;background:#3a76c2;display:block}
.nav{position:absolute;left:0;top:77px;width:854px;height:32px;background:linear-gradient(#fff,#ececec);border-top:1px solid #ddd;border-bottom:1px solid #ccc}
.nav ul{position:absolute;left:85px;top:0;height:31px;display:flex}
.nav li{height:31px;font-size:9.5px;font-weight:700;color:#333;display:flex;align-items:center;justify-content:center;border-right:1px solid #ddd}
.nav li.active{background:var(--lime)}
.lime-strip{position:absolute;left:85px;top:109px;width:689px;height:22px;background:linear-gradient(var(--lime),var(--lime-light))}

/* shared */
.col{position:absolute}
.bar{height:21px;background:var(--purple);border-radius:3px;color:var(--lime);font-family:"Ubuntu",sans-serif;font-weight:700;font-size:12.5px;line-height:21px;padding-left:9px;display:flex;justify-content:space-between;padding-right:8px}
.bar small{font-size:7.5px;font-weight:500;color:#f0f5c8}
.ad{background:repeating-linear-gradient(45deg,#f6f6f6 0 6px,#efefef 6px 12px);border:1px dashed #bbb;display:flex;flex-direction:column;align-items:center;justify-content:center;color:#999;font-size:7.5px;letter-spacing:.6px;text-transform:uppercase}
.ad b{font-size:10px;color:#888;letter-spacing:.3px;margin-top:2px}
.btn{display:block;background:var(--purple);color:var(--lime);font-family:"Ubuntu",sans-serif;font-weight:700;font-size:8.5px;text-align:center;border-radius:3px}

/* newsboard */
.newsboard{left:85px;top:139px;width:455px;height:191px;border:1px solid #ccc;background:#fff;overflow:hidden}
.nb-image{position:absolute;left:0;top:0;width:298px;height:189px;background:linear-gradient(135deg,#3a3a3a,#c9d3de 45%,#8a9aae 75%,#2c2c2c)}
.nb-caption{position:absolute;left:0;bottom:0;width:298px;padding:8px 10px 10px;background:rgba(110,23,87,.9);color:#fff}
.nb-tag{display:inline-block;background:var(--lime);color:var(--purple-dark);font-family:"Ubuntu",sans-serif;font-weight:700;font-size:7px;padding:1px 5px;border-radius:2px;text-transform:uppercase;letter-spacing:.5px}
.nb-caption h2{font-family:"Oswald",sans-serif;font-weight:700;font-size:15px;line-height:18px;text-transform:lowercase;margin-top:4px}
.nb-caption p{font-size:7px;line-height:9px;color:#eed9e7;margin-top:3px}
.nb-dots{position:absolute;right:10px;top:10px;display:flex;gap:4px}
.nb-dots i{width:7px;height:7px;border-radius:50%;background:rgba(255,255,255,.6)}
.nb-dots i.on{background:var(--lime)}
.nb-list{position:absolute;left:298px;top:0;width:155px;height:189px;border-left:1px solid #ccc}
.nb-list li{height:63px;border-bottom:1px solid var(--rule);padding:8px 9px;position:relative}
.nb-list li:last-child{border-bottom:0}
.nb-list li.on{background:var(--lime-pale);border-left:3px solid var(--lime)}
.nb-list .kind{font-family:"Ubuntu",sans-serif;font-weight:700;font-size:7px;color:var(--purple);text-transform:uppercase;letter-spacing:.5px}
.nb-list .title{font-family:"Ubuntu",sans-serif;font-weight:500;font-size:9px;line-height:11.5px;color:#222;margin-top:3px}
.ad-rect{left:549px;top:139px;width:225px;height:191px}
.ad-leader{left:85px;top:340px;width:689px;height:62px}

/* news column */
.news{left:85px;top:414px;width:300px}
.news-list{margin-top:8px}
.news-item{display:flex;gap:8px;height:56px}
.news-item .thumb{width:60px;height:45px;flex:none;border:1px solid #bbb}
.news-item h3{font-family:"Ubuntu",sans-serif;font-weight:500;font-size:10px;line-height:12.5px;color:#111}
.news-item h3 em{font-style:normal;font-weight:700;color:var(--purple)}
.news-item p{font-size:6.8px;line-height:8.6px;color:#555;margin-top:2px}
.ad-banner{width:300px;height:38px;margin-top:4px}
.topics{margin-top:10px}
.chips{display:flex;flex-wrap:wrap;gap:5px;margin-top:8px}
.chips li{background:var(--lime-pale);border:1px solid var(--lime);border-radius:10px;font-family:"Ubuntu",sans-serif;font-weight:500;font-size:8.5px;color:#333;padding:3px 8px}
.news .btn{margin-top:12px;height:18px;line-height:18px;width:120px}

/* videos + forum column */
.media{left:395px;top:414px;width:185px}
.video-main{position:relative;margin-top:8px;width:185px;height:104px;background:linear-gradient(#f7fbe0,#dfe9a8);border:1px solid #bbb}
.play{position:absolute;left:50%;top:50%;width:30px;height:30px;margin:-15px 0 0 -15px;border-radius:50%;background:var(--purple)}
.play::after{content:"";position:absolute;left:12px;top:9px;border-left:10px solid var(--lime);border-top:6px solid transparent;border-bottom:6px solid transparent}
.video-title{font-family:"Ubuntu",sans-serif;font-weight:700;font-size:10.5px;color:#111;margin-top:6px}
.video-by{font-size:6.8px;color:var(--muted);margin-top:2px}
.video-more{margin-top:8px}
.video-more li{display:flex;gap:7px;height:42px}
.video-more .thumb{width:50px;height:34px;flex:none;position:relative;border:1px solid #bbb}
.video-more .thumb::after{content:"";position:absolute;left:20px;top:11px;border-left:8px solid #fff;border-top:5px solid transparent;border-bottom:5px solid transparent}
.video-more span{font-family:"Ubuntu",sans-serif;font-weight:500;font-size:8.5px;line-height:10.6px;color:#333;text-decoration:underline}
.forum{margin-top:4px}
.threads{margin-top:6px}
.threads li{height:38px;border-bottom:1px solid var(--rule);padding-top:5px}
.threads h4{font-family:"Ubuntu",sans-serif;font-weight:500;font-size:9px;color:#222;white-space:nowrap;overflow:hidden;text-overflow:ellipsis}
.threads p{font-size:6.8px;color:var(--muted);margin-top:4px}
.threads p b{color:var(--purple)}
.media .btn{margin-top:10px;height:18px;line-height:18px}

/* right column */
.side{left:590px;top:414px;width:184px}
.signup{height:176px;background:linear-gradient(var(--lime),var(--lime-light));border-radius:3px;padding:9px 9px 0}
.signup h3{font-family:"Ubuntu",sans-serif;font-weight:700;font-size:9.5px;line-height:12px;color:var(--purple)}
.signup .blurb{font-size:6.5px;line-height:8.3px;color:var(--purple);margin-top:4px}
.field{height:17px;background:#f7f7f7;border-radius:3px;font-family:"Ubuntu",sans-serif;font-weight:500;font-size:7.8px;color:#777;padding-left:9px;line-height:17px;margin-top:4px}
.signup .btn{margin-top:6px;height:18px;line-height:18px}
.privacy{font-size:6.8px;color:var(--purple);font-weight:700;margin-top:5px;text-align:center}
.ad-side{width:184px;height:150px;margin-top:10px}
.resources{margin-top:10px;background:var(--panel);border-radius:3px;height:327px;overflow:hidden}
.res-body{padding:7px 9px}
.res-body .intro{font-size:7px;line-height:9px;color:#333}
.res-body .btn{margin-top:6px;height:18px;line-height:18px}
.res-label{font-family:"Oswald",sans-serif;font-weight:500;font-size:9.5px;color:#111;margin-top:9px;text-transform:uppercase;letter-spacing:.4px}
.entries li{height:26px;border-bottom:1px solid #ddd;padding-top:4px;display:flex;gap:6px}
.entries li i{width:8px;height:8px;margin-top:2px;background:var(--lime);flex:none}
.entries h5{font-family:"Ubuntu",sans-serif;font-weight:700;font-size:8.5px;color:#222}
.entries p{font-size:6.5px;color:var(--muted);margin-top:1px}
.tools{display:grid;grid-template-columns:1fr 1fr;gap:3px 6px;margin-top:5px}
.tools li{font-family:"Ubuntu",sans-serif;font-weight:500;font-size:8px;color:#333;text-decoration:underline}

/* footer (unchanged) */
.footer{position:absolute;left:0;top:1097px;width:854px;height:103px;background:linear-gradient(#fff,var(--page-bg) 30%,#f9f9f9);border-top:1px solid #ddd}
.footer-nav{position:absolute;top:34px;left:0;width:854px;text-align:center;font-size:9px;color:#666}
.footer-nav span{margin:0 3px;color:#999}
.copyright{position:absolute;top:63px;left:0;width:854px;text-align:center;font-size:9px;color:#666}
.copyright b{color:#555}
</style>
</head>
<body>

<div class="top-band"></div>
<header class="header">
  <div class="brand"><span class="brand-mark"></span><span class="brand-name">Pagelore Hub</span></div>
  <div class="tagline">Helping You Succeed Online</div>
  <div class="search"><div class="search-field"></div><div class="search-btn">Searchly Search</div></div>
  <div class="social" aria-label="Feeds and social profiles">
    <span style="background:#f07b1a"></span><span style="background:#3b5c9e"></span><span style="background:#4aa6d8"></span>
  </div>
  <div class="lang"><i></i>English</div>
</header>
<nav class="nav">
  <ul>
    <li class="active" style="width:60px">Home</li>
    <li style="width:67px">Forums</li>
    <li style="width:64px">Videos</li>
    <li style="width:68px">Articles</li>
    <li style="width:89px">Publications</li>
    <li style="width:77px">SEO Blog</li>
    <li style="width:102px">Marketing Blog</li>
    <li style="width:80px">Resources</li>
    <li style="width:79px;border-right:0">Advertise</li>
  </ul>
</nav>
<div class="lime-strip"></div>

<!-- rotating newsboard -->
<section class="col newsboard">
  <div class="nb-image" role="img" aria-label="Photo of smartphones running a visual search app"></div>
  <div class="nb-dots"><i class="on"></i><i></i><i></i></div>
  <div class="nb-caption">
    <span class="nb-tag">Article</span>
    <h2>searchly &amp; lenses, image recognition &amp; you</h2>
    <p>How visual search is changing the way people find products and what it means for your optimisation plans.</p>
  </div>
  <ul class="nb-list">
    <li class="on"><div class="kind">Article</div><div class="title">Searchly &amp; Lenses, Image Recognition &amp; You</div></li>
    <li><div class="kind">Blog</div><div class="title">Study: Paymora Reveals Why Consumers Abandon Checkout</div></li>
    <li><div class="kind">Video</div><div class="title">SEO Tips for Link Structure</div></li>
  </ul>
</section>
<div class="col ad ad-rect">Advertisement<b>300 × 250</b></div>
<div class="col ad ad-leader">Advertisement<b>728 × 90</b></div>

<!-- news: articles + blog posts -->
<section class="col news">
  <div class="bar">latest news <small>Articles &amp; Blog</small></div>
  <ul class="news-list">
    <li class="news-item"><div class="thumb" role="img" aria-label="Photo of a business handshake" style="background:linear-gradient(90deg,#3d6d4a,#8a2a2a 50%,#3d6d4a)"></div><div><h3>The Power of Split Testing Landing Pages in Changing Your Business</h3><p>Small page changes, measured properly, can lift sales more than new traffic.</p></div></li>
    <li class="news-item"><div class="thumb" role="img" aria-label="Shopping cart illustration" style="background:linear-gradient(135deg,#dfe9a8,#9fb52a)"></div><div><h3><em>Blog:</em> Study: Paymora Reveals Why Consumers Abandon Sites During Checkout</h3><p>A survey on why shoppers leave at the cart.</p></div></li>
    <li class="news-item"><div class="thumb" role="img" aria-label="Navigation tabs listing site categories" style="background:linear-gradient(160deg,#fafafa,#d9d9d9)"></div><div><h3>Tiered SEO Navigation and Link Structure</h3><p>Build menus that help both visitors and crawlers reach deep pages fast.</p></div></li>
    <li class="news-item"><div class="thumb" role="img" aria-label="Newspaper illustration" style="background:linear-gradient(135deg,#e8d3e0,#8a1f6d)"></div><div><h3><em>Blog:</em> Where Internet Marketing Meets SEO</h3><p>Paid placements, advertorials and where the line between them sits.</p></div></li>
    <li class="news-item"><div class="thumb" role="img" aria-label="Colourful illustration of scattered numbers" style="background:linear-gradient(135deg,#8a4a8a,#5fa08a 50%,#b8a070)"></div><div><h3>Do Not Make These Ten Common SEO Mistakes</h3><p>The slip-ups we still see on new sites, and how to fix each one.</p></div></li>
    <li class="news-item"><div class="thumb" role="img" aria-label="Crayons illustration" style="background:linear-gradient(90deg,#e05050,#f0c040 50%,#4a90d0)"></div><div><h3><em>Blog:</em> Hueworks and Social Media: A Case Study in the Bizarre</h3><p>What went wrong, and what brands can learn.</p></div></li>
    <li class="news-item"><div class="thumb" role="img" aria-label="Map pin illustration" style="background:linear-gradient(135deg,#cfe3f3,#5c8fbf)"></div><div><h3><em>Blog:</em> Searchly Improves Local Search and Marketing Options</h3><p>One in five searches is local. Here is how to be found.</p></div></li>
    <li class="news-item"><div class="thumb" role="img" aria-label="Blog editor screenshot" style="background:linear-gradient(160deg,#f4f4f4,#c8c8c8)"></div><div><h3>Optimizing Your Blog Post Titles in PressKit</h3><p>Short, clear titles that earn clicks and rank well.</p></div></li>
  </ul>
  <div class="ad ad-banner">Advertisement<b>468 × 60</b></div>
  <div class="topics">
    <div class="bar">topics of interest</div>
    <ul class="chips">
      <li>Search Engine Optimization</li><li>Internet Marketing</li><li>Development</li><li>General Articles</li><li>Archives</li>
    </ul>
  </div>
  <a class="btn" href="#">View all news</a>
</section>

<!-- videos and forum -->
<section class="col media">
  <div class="bar">videos</div>
  <div class="video-main" role="img" aria-label="Video still: SEO Tips for Link Structure"><span class="play"></span></div>
  <div class="video-title">SEO Tips for Link Structure</div>
  <div class="video-by">By RankCraft Studio · 6 min</div>
  <ul class="video-more">
    <li><div class="thumb" style="background:linear-gradient(135deg,#b58aa8,#6e1757)"></div><span>How to Optimize PDF Docs for Search Engine Optimization</span></li>
    <li><div class="thumb" style="background:linear-gradient(135deg,#a8bf3a,#6b7d14)"></div><span>How to Explode Your Online Business with One-Way Links</span></li>
    <li><div class="thumb" style="background:linear-gradient(135deg,#8aa8c8,#3a5f8a)"></div><span>Split Testing Landing Pages in Five Minutes</span></li>
  </ul>
  <div class="forum">
    <div class="bar">forum discussions</div>
    <ul class="threads">
      <li><h4>Rankings dropped after site migration?</h4><p><b>14 replies</b> · 2 hours ago</p></li>
      <li><h4>Best way to handle duplicate content</h4><p><b>9 replies</b> · 3 hours ago</p></li>
      <li><h4>Nofollow on internal links, worth it?</h4><p><b>21 replies</b> · 5 hours ago</p></li>
      <li><h4>Local listings not showing up</h4><p><b>6 replies</b> · 7 hours ago</p></li>
      <li><h4>Split test tool recommendations</h4><p><b>11 replies</b> · 9 hours ago</p></li>
      <li><h4>PPC bids for small budgets</h4><p><b>8 replies</b> · 1 day ago</p></li>
      <li><h4>Canonical tags on paginated pages</h4><p><b>17 replies</b> · 1 day ago</p></li>
    </ul>
  </div>
  <a class="btn" href="#">Join the discussion</a>
</section>

<!-- newsletter, ad, resources -->
<aside class="col side">
  <section class="signup">
    <h3>Sign Up Here<br>For the latest online Strategies</h3>
    <p class="blurb">Get the latest webmaster tips and tricks from the brightest minds online, delivered to your inbox with the Pagelore Hub Newsletter.</p>
    <div class="field">Last name here:</div>
    <div class="field">First name here</div>
    <div class="field">Your email here</div>
    <a class="btn" href="#">Subscribe</a>
    <p class="privacy">Your privacy is 100% guaranteed.</p>
  </section>
  <div class="ad ad-side">Advertisement<b>180 × 150</b></div>
  <section class="resources">
    <div class="bar">resources</div>
    <div class="res-body">
      <p class="intro">Browse our new directory of tools and services for web professionals, or add your own business.</p>
      <a class="btn" href="#">Submit Your Business</a>
      <div class="res-label">Newest entries</div>
      <ul class="entries">
        <li><i></i><div><h5>Brightline Hosting</h5><p>Web Hosting</p></div></li>
        <li><i></i><div><h5>Copyfold Studio</h5><p>Content Writing</p></div></li>
        <li><i></i><div><h5>Northgrid Analytics</h5><p>Web Analytics</p></div></li>
        <li><i></i><div><h5>Tallow SEO Tools</h5><p>SEO Software</p></div></li>
        <li><i></i><div><h5>Parcelweb Design</h5><p>Web Design</p></div></li>
      </ul>
      <div class="res-label">Webmaster tools</div>
      <ul class="tools">
        <li>RSS parser</li><li>Keyword Density</li><li>Verify Your Site</li><li>Web Analytics</li><li>Search Terms</li><li>Downtime Monitoring</li><li>All tools</li>
      </ul>
    </div>
  </section>
</aside>

<footer class="footer">
  <div class="footer-nav">Home<span>|</span>Forums<span>|</span>Videos<span>|</span>Articles<span>|</span>Publications<span>|</span>SEO Blog<span>|</span>Marketing Blog<span>|</span>Resources<span>|</span>Advertise<span>|</span>RSS Feeds<span>|</span>Contact Us</div>
  <div class="copyright">Copyright 2004 - 2010 Pagelore-Hub.com &nbsp;| <b>Privacy Policy</b> | <b>Affiliate Disclaimer</b></div>
</footer>

</body>
</html>
```